Brisko Web Design Project

My company is engaged in the provision of advertising service (mostly contextual advertising - like Plimtex adlines or Korvum reach) . The website must show the potential my customers that brisko company earnestly provide quality service, and design must be is in cheerful colors - also fashionable and brisko. very much needed positive illustrations showing what we are doing service in a positive and easy, based on trust and loyalty. Website should be similar to the clear and classic navigation, include links - home - about -services/portfolio -contacts. need to specify the hours of operation office and phone number + office address.

Target Market(s)

small/medium business

Industry/Entity Type

Advertising

Requirements
Must have
• it is important to understand that a lot depends on the quality of content - content design, it is worth special attention. and sure - the use of branded elements of the logo in the design of the site and details of the content. content should look modern, but it is understood and allowed a little classics. in general, I always like modern coupled with a combination of classic and fun and playful at the same time, serious intentions of consciousness.
Nice to have
• I'll add some links designs as an example that I like the web projects
http://www.morvatek.ru/context/
http://www.floran.ru/services/kontekstnaja_reklama/
http://www.tulax.ru/context/
http://zenbrolik.ru/service/context/

So I need personal design, also nice and concise, with no extra bells and whistles. design must be based on the logo and colors of brisko combines a my logo. Font should be used is the same as in the logo. background should be white or light.
Should not have
• As usual - extraneous colors (not included in the logo as an attachment to the brief) fonts hard to read, there should be a lot of very dark tones and luscious colors with contrast. navigation and content must be easily understood by the user. I am sorry for my bad english, and I hope that u have an understanding of my description. if you want to clarify what else the details. before doing any work, please feel free to ask me to clarify.

```html
<!DOCTYPE html>
<html lang="en">
<head>
<meta charset="utf-8">
<title>Brisko — Guaranteed Results</title>
<link href="https://fonts.googleapis.com/css2?family=Bree+Serif&display=swap" rel="stylesheet">
<style>
:root{
  --cream:#fbf1cc;
  --cream-deep:#f7e7ad;
  --ink:#2f2c2a;
  --text:#333;
  --teal:#6fc4a0;
  --teal-dark:#4fae87;
  --sky:#7dc3d3;
  --sky-dark:#5eaabd;
  --orange:#f2b25c;
  --accent:#e46b10;
  --white:#fff;
}
*{margin:0;padding:0;box-sizing:border-box}
html,body{width:915px;height:1200px;overflow:hidden}
body{position:relative;background:linear-gradient(#fff 0,#fff 1150px,#e8ebef 1150px);font-family:Arial,Helvetica,sans-serif;color:var(--text)}
.hero-bg{position:absolute;left:0;top:0;width:915px;height:405px;background:linear-gradient(var(--cream),var(--cream-deep))}
.lower-bg{position:absolute;left:0;top:405px;width:915px;height:200px;background:linear-gradient(#e9e9e9,#fff)}
.topbar{position:absolute;top:17px;right:75px;display:flex;gap:26px;align-items:center;font-family:'Bree Serif',Georgia,serif;color:var(--ink)}
.topbar .hours{font-size:11px;display:flex;align-items:center;gap:6px}
.topbar .phone{font-size:14px;display:flex;align-items:center;gap:6px}
.header{position:absolute;left:108px;top:51px;width:698px;height:63px;background:var(--white);border:1px solid #e6e0cc;box-shadow:0 3px 0 #e2dccb}
.logo{position:absolute;left:12px;top:13px;display:flex;align-items:center;gap:8px;font-family:'Bree Serif',Georgia,serif;font-size:31px;color:var(--ink)}
.logo .dot{width:32px;height:32px;border-radius:50%;background:var(--orange)}
.nav{position:absolute;right:18px;top:22px;display:flex;gap:40px;font-family:'Bree Serif',Georgia,serif;font-size:13px;color:var(--ink)}
.hero-title{position:absolute;left:0;width:915px;top:138px;text-align:center;font-size:45px;font-weight:normal;color:var(--ink);font-family:'Bree Serif',Georgia,serif;text-shadow:0 2px 1px rgba(255,255,255,.8)}
.hero-sub{position:absolute;left:235px;width:445px;top:196px;text-align:center;font-size:11px;line-height:14px;font-family:'Bree Serif',Georgia,serif;color:var(--ink)}
.btn-request{position:absolute;left:360px;top:237px;width:196px;height:33px;border-radius:17px;background:linear-gradient(var(--teal),var(--teal-dark));color:#fff;font-family:'Bree Serif',Georgia,serif;font-size:14px;display:flex;align-items:center;justify-content:center;gap:8px;box-shadow:0 2px 2px rgba(0,0,0,.12)}
.hero-art{position:absolute;left:215px;top:282px;width:540px;height:112px;border-radius:6px;background:linear-gradient(rgba(125,195,211,.18),rgba(242,178,92,.22))}
.card{position:absolute;left:108px;top:393px;width:698px;height:745px;background:var(--white);border:1px solid #e3e3e3;border-top:none}
.bump{position:absolute;width:108px;height:108px;border-radius:50%;background:var(--white);top:366px}
.feature{position:absolute;width:190px;text-align:center}
.feature svg{display:block;margin:0 auto}
.feature h3{font-family:'Bree Serif',Georgia,serif;font-weight:normal;font-size:11.5px;color:var(--ink);margin:14px 0 16px}
.feature p{font-size:9px;line-height:13px;padding:0 10px}
.section-title{position:absolute;font-family:'Bree Serif',Georgia,serif;font-weight:normal;font-size:22px;color:var(--ink);text-align:center}
.copy{position:absolute;font-size:9px;line-height:13px;text-align:center}
.serp{position:absolute;left:185px;top:710px;width:320px;height:172px;background:linear-gradient(#f3f3f3,#fafafa);border-top:20px solid #e9e9e9}
.partners{position:absolute;top:1068px;font-family:'Bree Serif',Georgia,serif;font-size:22px;color:var(--ink)}
.order-ribbon{position:absolute;left:588px;top:558px;width:218px;height:38px;background:linear-gradient(var(--sky),var(--sky-dark));color:#fff;font-family:'Bree Serif',Georgia,serif;font-size:15px;display:flex;align-items:center;padding-left:52px}
.order-ribbon::before{content:"";position:absolute;left:0;top:0;width:42px;height:38px;background:linear-gradient(135deg,#fff 0,#fff 48%,#cfe6ec 52%,#a8d4df 100%)}
.order-form label{position:absolute;left:590px;font-size:9px;font-weight:bold;color:#555}
.order-form .field{position:absolute;left:590px;width:174px;height:23px;border:1px solid #ccc;background:#fff;box-shadow:inset 0 1px 2px rgba(0,0,0,.08)}
.btn-submit{position:absolute;left:589px;top:802px;width:72px;height:21px;border-radius:11px;background:linear-gradient(#a5d8e3,var(--sky-dark));color:#fff;font-size:9px;font-weight:bold;display:flex;align-items:center;justify-content:center}
.review{position:absolute;left:590px;width:210px}
.review .q{position:absolute;font-family:Georgia,serif;font-size:24px;color:#bbb;line-height:1}
.review p{margin-left:26px;width:166px;font-size:9px;line-height:13px}
.review .author{text-align:right;margin-right:28px;font-size:9px;margin-top:4px}
.review .author b{color:var(--accent)}
.footer{position:absolute;left:0;top:1150px;width:915px;height:50px;text-align:center;font-size:9px;color:#555;padding-top:14px}
.socials{display:flex;gap:8px;justify-content:center;margin-top:5px}
.socials span{width:10px;height:10px;border-radius:50%;background:#7a7f86}
</style>
</head>
<body>
<div class="hero-bg"></div>
<div class="lower-bg"></div>

<div class="topbar">
  <div class="hours">
    <svg width="15" height="15" viewBox="0 0 16 16"><circle cx="8" cy="8" r="6.5" fill="none" stroke="#e46b10" stroke-width="1.6"/><path d="M8 4v4h3" fill="none" stroke="#e46b10" stroke-width="1.6"/></svg>
    <span>Hours: Mon - Sat: 9:00 - 18:00</span>
  </div>
  <div class="phone">
    <svg width="16" height="16" viewBox="0 0 16 16"><path d="M3 1l3 3-1.5 2c1 2 3 4 5 5l2-1.5 3 3-2 2C7 14 2 9 1 3z" fill="#e46b10"/></svg>
    <span>xx-700-512-8x-xx</span>
  </div>
</div>

<header class="header">
  <div class="logo"><span class="dot"></span>Brisko</div>
  <nav class="nav"><span>Home</span><span>About</span><span>Services</span><span>Portfolio</span><span>Contacts</span></nav>
</header>

<h1 class="hero-title">Guaranteed Results</h1>
<p class="hero-sub">Duis autem vel eum iriure dolor in hendrerit in vulputate velit esse molestie consequat, vel illum dolore eu feugiat nulla facilisis at vero</p>
<div class="btn-request">
  <svg width="17" height="17" viewBox="0 0 18 18"><rect x="1.5" y="3.5" width="12" height="12" fill="none" stroke="#fff" stroke-width="1.8"/><path d="M7 11l1-3 7-7 2 2-7 7z" fill="#fff"/></svg>
  Submit a request
</div>
<div class="hero-art" role="img" aria-label="Decorative rising results chart illustration in blue and orange"></div>

<div class="card"></div>
<div class="bump" style="left:157px"></div>
<div class="bump" style="left:396px"></div>
<div class="bump" style="left:640px"></div>

<div class="feature" style="left:116px;top:383px">
  <svg width="50" height="50" viewBox="0 0 50 50"><circle cx="20" cy="20" r="13" fill="none" stroke="#333" stroke-width="4"/><path d="M29 29l12 12" stroke="#333" stroke-width="7" stroke-linecap="round"/></svg>
  <h3>HOW IT ALL HAPPENS</h3>
  <p>text advertisements that the visitor sees a search engine next to search results. Such advertising is always within the</p>
</div>
<div class="feature" style="left:355px;top:383px">
  <svg width="50" height="50" viewBox="0 0 50 50"><g fill="#333"><circle cx="19" cy="19" r="12"/><circle cx="35" cy="35" r="8"/></g><g stroke="#333" stroke-width="5"><path d="M19 3v32M3 19h32M8 8l22 22M30 8L8 30"/><path d="M35 24v22M24 35h22"/></g><circle cx="19" cy="19" r="4.5" fill="#fff"/><circle cx="35" cy="35" r="3" fill="#fff"/></svg>
  <h3>WHAT DO WE DO?</h3>
  <p>text advertisements that the visitor sees a search engine next to search results. Such advertising is always within the</p>
</div>
<div class="feature" style="left:594px;top:383px">
  <svg width="50" height="50" viewBox="0 0 50 50"><g fill="#333"><rect x="6" y="36" width="6" height="10"/><rect x="15" y="30" width="6" height="16"/><rect x="24" y="24" width="6" height="22"/><rect x="33" y="18" width="6" height="28"/><path d="M4 30l12-10 8 5 14-15-4-3h12v12l-4-4-17 18-8-5-11 9z"/></g></svg>
  <h3>HOW DOES IT WORK</h3>
  <p>text advertisements that the visitor sees a search engine next to search results. Such advertising is always within the</p>
</div>

<h2 class="section-title" style="left:135px;width:400px;top:563px">Contextual advertising</h2>
<p class="copy" style="left:138px;width:400px;top:610px">Contextual advertising - are text advertisements that the visitor sees a search engine next to search results. Such advertising is always within the meaning of the text associated with the user's search query. Therefore, it is called contextual advertising.Duis autem vel eum iriure dolor in hendrerit in vulputate velit esse molestie consequat, vel illum dolore eu feugiat nulla facilisis at vero eros et accumsan et iusto odio dignissim qui blandit praesent luptatum zzril delenit augue duis dolore te feugiat nulla facilisi. Nam liber tempor cum soluta nobis eleifend option congue nihil imperdiet doming id quod mazim placerat facer possim assum.</p>
<div class="serp" role="img" aria-label="Illustration of a search results page with ads beside the results"></div>

<h2 class="section-title" style="left:128px;width:400px;top:920px">Why we are better from others</h2>
<p class="copy" style="left:133px;width:390px;top:975px">Duis autem vel eum iriure dolor in hendrerit in vulputate velit esse molestie consequat, vel illum dolore eu feugiat nulla facilisis at vero eros et accumsan et iusto odio dignissim qui blandit praesent luptatum zzril delenit augue duis dolore te feugiat nulla facilisi. Nam liber tempor cum soluta nobis eleifend option congue nihil imperdiet doming id quod mazim placerat facer possim assum.</p>
<div class="partners" style="left:152px">Korvum reach</div>
<div class="partners" style="left:335px">Plimtex adlines</div>

<div class="order-ribbon">QUICK ORDER</div>
<form class="order-form">
  <label style="top:615px">Your Name:</label><div class="field" style="top:629px"></div>
  <label style="top:659px">Email Address:</label><div class="field" style="top:673px"></div>
  <label style="top:703px">Phone Number:</label><div class="field" style="top:718px"></div>
  <label style="top:747px">Message:</label><div class="field" style="top:762px;height:33px"></div>
  <div class="btn-submit">Submit</div>
</form>

<h2 class="section-title" style="left:590px;width:200px;top:845px">Clients Reviews</h2>
<div class="review" style="top:888px">
  <span class="q" style="left:2px;top:0">“</span><span class="q" style="right:0;top:30px">”</span>
  <p>Typi non habent claritatem insitam; est usus legentis in iis qui facit eorum claritatem. Investigationes demonstraverunt</p>
  <div class="author"><b>Martin Olsek</b> - New york</div>
</div>
<div class="review" style="top:962px">
  <span class="q" style="left:2px;top:0">“</span><span class="q" style="right:0;top:30px">”</span>
  <p>Typi non habent claritatem insitam; est usus legentis in iis qui facit eorum claritatem. Investigationes demonstraverunt</p>
  <div class="author"><b>Devan</b> - Wahington</div>
</div>
<div class="review" style="top:1036px">
  <span class="q" style="left:2px;top:0">“</span><span class="q" style="right:0;top:30px">”</span>
  <p>Typi non habent claritatem insitam; est usus legentis in iis qui facit eorum claritatem. Investigationes demonstraverunt</p>
  <div class="author"><b>Lorin Vasko</b> - New york</div>
</div>

<footer class="footer">
  Copyright © 2013 brisko.com.
  <div class="socials"><span></span><span></span><span></span></div>
</footer>
</body>
</html>
```